Visitenkarten-Design für private Praxis für Sprachtherapie
Zielgruppe
Private Praxis für Sprachtherapie (Logopädie)
Aufgabenstellung
Siehe PDF der Anlage.

```html
<!DOCTYPE html>
<html lang="de">
<head>
<meta charset="utf-8">
<title>Visitenkarte – Praxis für Sprachtherapie</title>
<link href="https://fonts.googleapis.com/css2?family=Fira+Sans:wght@300;400;600;700;800&display=swap" rel="stylesheet">
<style>
  :root {
    --navy: #223567;
    --navy-text: #1c2c6e;
    --ink: #3a3a3a;
    --muted: #6b6b6b;
    --cloud-light: #eeeff0;
    --cloud-mid: #dcdee0;
    --field: #e6e6f0;
    --label: #aab0c2;
    --border: #7a7a7a;
    --paper: #ffffff;
  }
  * { box-sizing: border-box; margin: 0; padding: 0; }
  html, body { width: 848px; height: 1200px; overflow: hidden; background: var(--paper); }
  body { position: relative; font-family: "Fira Sans", sans-serif; }

  .card { position: absolute; left: 214px; width: 340px; height: 223px; }
  .card--front { top: 197px; border: 1px solid var(--border); background: var(--paper); overflow: hidden; }
  .card--back { top: 462px; background: var(--navy); }

  .theme-area {
    position: absolute; left: 10px; top: 52px; width: 120px; height: 118px;
    background: radial-gradient(ellipse at 50% 50%, var(--cloud-mid) 0%, var(--cloud-light) 55%, var(--paper) 100%);
  }

  .brand {
    position: absolute; left: 145px; top: 36px;
    display: flex; align-items: center; gap: 8px;
  }
  .brand__name { font-size: 17px; font-weight: 600; color: var(--navy-text); }
  .brand__dot { width: 26px; height: 26px; border: 1.5px solid var(--navy-text); border-radius: 50%; }

  .address { position: absolute; left: 145px; top: 91px; font-size: 11px; line-height: 14.4px; font-weight: 300; color: var(--muted); font-style: normal; }
  .address .practice { color: var(--ink); }
  .address .owner { color: var(--navy-text); font-weight: 600; }

  .contact { position: absolute; left: 145px; top: 154px; list-style: none; font-size: 11px; line-height: 14.4px; font-weight: 300; color: var(--muted); }
  .contact li { display: flex; align-items: center; }
  .contact svg { width: 12px; height: 10px; margin-right: 7px; flex: none; }

  .bottom-band { position: absolute; left: 0; right: 0; bottom: 0; height: 11px; background: var(--navy); }

  .appointments__title { position: absolute; left: 25px; top: 21px; font-size: 11px; font-weight: 700; color: #fff; }
  .appointments__label { position: absolute; top: 45px; font-size: 8.2px; color: var(--label); }
  .appointments__field { position: absolute; width: 81px; height: 16px; background: var(--field); }
</style>
</head>
<body>

<section class="card card--front">
  <div class="theme-area" role="img" aria-label="Dekorative Wortwolke mit Begriffen der Sprachtherapie in Grautönen"></div>

  <div class="brand">
    <span class="brand__name">Helga Vorndran</span>
    <span class="brand__dot"></span>
  </div>

  <address class="address">
    <div class="practice">Praxis für Sprachtherapie</div>
    <div class="owner">Helga Vorndran</div>
    <div>Ahornweg 14</div>
    <div>32791 Lindental</div>
  </address>

  <ul class="contact">
    <li>
      <svg viewBox="0 0 12 10"><path d="M2.5 0.5 L4.3 0.3 L5 2.6 L3.8 3.4 C4.4 5 5.4 6.2 6.8 7 L7.8 5.9 L9.9 6.9 L9.6 8.7 C5.6 9.2 1.8 5 2.5 0.5 Z" fill="var(--navy-text)"/></svg>
      05206 48 19 62
    </li>
    <li>
      <svg viewBox="0 0 12 10"><rect x="0.6" y="1" width="10.8" height="8" fill="none" stroke="var(--navy-text)" stroke-width="1"/><path d="M0.6 1 L6 5.6 L11.4 1 M0.6 9 L4.4 4.4 M11.4 9 L7.6 4.4" fill="none" stroke="var(--navy-text)" stroke-width="0.9"/></svg>
      info@logopaedie-vorndran.de
    </li>
    <li>
      <svg viewBox="0 0 12 10"><g fill="none" stroke="var(--navy-text)" stroke-width="0.9"><circle cx="6" cy="5" r="4.5"/><ellipse cx="6" cy="5" rx="2" ry="4.5"/><path d="M1.5 5 H10.5 M2.2 2.7 H9.8 M2.2 7.3 H9.8"/></g></svg>
      www.logopaedie-vorndran.de
    </li>
  </ul>

  <div class="bottom-band"></div>
</section>

<section class="card card--back appointments">
  <h2 class="appointments__title">Ihre nächsten Termine:</h2>
  <span class="appointments__label" style="left:25px">Wochentag</span>
  <span class="appointments__label" style="left:112px">Datum</span>
  <span class="appointments__label" style="left:201px">Uhrzeit</span>

  <div class="appointments__field" style="left:25px;top:57px"></div>
  <div class="appointments__field" style="left:112px;top:57px"></div>
  <div class="appointments__field" style="left:200px;top:57px"></div>

  <div class="appointments__field" style="left:25px;top:79px"></div>
  <div class="appointments__field" style="left:112px;top:79px"></div>
  <div class="appointments__field" style="left:200px;top:79px"></div>

  <div class="appointments__field" style="left:25px;top:101px"></div>
  <div class="appointments__field" style="left:112px;top:101px"></div>
  <div class="appointments__field" style="left:200px;top:101px"></div>

  <div class="appointments__field" style="left:25px;top:124px"></div>
  <div class="appointments__field" style="left:112px;top:124px"></div>
  <div class="appointments__field" style="left:200px;top:124px"></div>

  <div class="appointments__field" style="left:25px;top:146px"></div>
  <div class="appointments__field" style="left:112px;top:146px"></div>
  <div class="appointments__field" style="left:200px;top:146px"></div>
</section>

</body>
</html>
```